French Tech Blog : Wordpress theme

I need a wordpress theme made, for a french tech blog like gadgetpulse.com or lampwright.com .. (the structure)

I will of course also need a logo that hold the identity of the website !

The blog's name is BrightOrchid.com

The tone should be in the dark blue..

Target Market(s)

affiliate marketers, web entrepreneurs, 70% male between 20 and 35

Industry/Entity Type

Tech

```html
<!DOCTYPE html>
<html lang="en">
<head>
<meta charset="utf-8">
<title>Bright Orchid</title>
<link href="https://fonts.googleapis.com/css2?family=PT+Sans:wght@400;700&family=Noto+Sans:wght@400;700&family=Questrial&display=swap" rel="stylesheet">
<style>
:root{
  --navy:#0b2747;
  --deep:#06152b;
  --blue:#0d5ea3;
  --blue-mid:#1a6fb8;
  --red:#d21f3c;
  --red-box:#e00d1f;
  --ink:#222;
  --grey:#8a8a8a;
  --line:#dcdcdc;
  --white:#fff;
}
*{margin:0;padding:0;box-sizing:border-box}
html,body{width:880px;height:1200px;overflow:hidden}
body{
  position:relative;
  background:radial-gradient(ellipse at 50% 30%,#15558f 0%,#0c3766 45%,#061a36 100%);
  font-family:"Noto Sans",sans-serif;color:var(--ink);
}
.page{position:absolute;left:56px;top:0;width:768px;height:1166px;background:var(--white)}
.header{height:100px;position:relative}
.logo{position:absolute;left:28px;top:38px;display:flex;align-items:center;gap:8px}
.logo-dot{width:26px;height:26px;border-radius:50%;background:var(--red)}
.logo-name{font-family:"Questrial",sans-serif;font-size:30px;color:var(--blue);line-height:1}
.banner{position:absolute;left:322px;top:20px;width:432px;height:48px;background:#141414;color:#fff;padding:3px 8px;font-family:"PT Sans",sans-serif}
.banner h3{font-size:11px;color:#4db0ff;font-weight:700}
.banner ul{list-style:none;font-size:6.5px;line-height:8px;font-weight:700;columns:2;width:340px}
.banner-bars{position:absolute;right:8px;bottom:4px}
.nav{height:34px;background:var(--navy);display:flex;align-items:center;position:relative}
.nav a{font-family:"PT Sans",sans-serif;color:#fff;text-decoration:none;font-size:11.5px;letter-spacing:.3px}
.nav .home{width:118px;height:34px;background:var(--blue-mid);display:flex;align-items:center;justify-content:center}
.nav .item{margin-left:36px}
.search{position:absolute;right:16px;top:7px;width:161px;height:20px;background:#fff;display:flex;justify-content:flex-end;align-items:center;padding-right:4px}
.main{position:absolute;left:12px;top:138px;width:487px}
.post{height:144px;border-bottom:1px solid var(--line);position:relative;padding-top:12px}
.post h2{font-family:"Questrial",sans-serif;font-weight:400;font-size:15px;color:var(--ink)}
.thumb{position:absolute;left:0;top:40px;width:94px;height:66px;background:linear-gradient(135deg,#3c8a97,#6db5b9 50%,#2e6b78)}
.excerpt{position:absolute;left:99px;top:40px;width:392px;font-size:9.3px;line-height:13px;color:var(--grey)}
.excerpt p+p{margin-top:5px}
.more{position:absolute;left:99px;top:110px;width:54px;height:17px;background:var(--blue);color:#fff;font-size:7.5px;font-weight:700;border-radius:3px;display:flex;align-items:center;justify-content:center}
.share{position:absolute;left:380px;top:114px;width:100px;height:11px;border:1px solid #bbb;font-size:6.5px;font-weight:700;display:flex;align-items:center;gap:3px;padding-left:3px}
.share i{width:7px;height:7px;display:block}
.divider{position:absolute;left:508px;top:138px;width:1px;height:888px;background:var(--line)}
.side{position:absolute;left:515px;top:0;width:246px}
.social{position:absolute;left:13px;top:146px;display:flex;gap:7px}
.social span{width:24px;height:24px;border-radius:4px;display:block}
.callout{position:absolute;left:12px;width:216px;height:39px;border:1px solid var(--line);display:flex;align-items:center;gap:8px;padding-left:10px;font-family:"PT Sans",sans-serif;font-weight:700;font-size:9px;color:var(--ink)}
.callout i{width:20px;height:20px;border-radius:50%;display:block}
.tabs{position:absolute;left:0;top:289px;width:246px;height:168px;background:var(--blue);padding:8px 8px 6px}
.tab-row{display:flex;font-size:11px;color:#fff;height:18px}
.tab-row span{padding:0 5px}
.tab-row .on{background:#fff;color:var(--ink)}
.tab-row .gap{margin-left:14px}
.tab-body{background:#fff;height:136px;padding:8px 0 0 12px}
.arrow-list{list-style:none;font-size:9.5px;color:var(--grey);line-height:13px}
.arrow-list li{padding-left:13px;position:relative}
.arrow-list li::before{content:"";position:absolute;left:0;top:4px;border-left:6px solid var(--navy);border-top:3px solid transparent;border-bottom:3px solid transparent}
.panel-head{position:absolute;left:0;width:246px;height:26px;background:var(--blue);color:#fff;font-family:"Questrial",sans-serif;font-size:12px;padding:7px 8px}
.featured{position:absolute;left:10px;top:516px;width:236px}
.featured li{margin-bottom:7px;line-height:13px}
.photo{position:absolute;left:29px;top:682px;width:187px;height:225px;background:linear-gradient(180deg,#b8c6cf 0%,#9a8c74 45%,#5d5a55 100%);border:1px solid #ccc}
.badge{position:absolute;top:926px;width:81px;height:75px}
.footer{position:absolute;left:0;top:1034px;width:768px;height:132px;background:var(--red);color:#fff}
.fcol{position:absolute;top:11px;font-size:10px;line-height:14.4px}
.fcol h4{font-family:"Questrial",sans-serif;font-weight:400;font-size:14px;margin-bottom:5px}
.fcol ul{list-style:none;padding-left:2px}
.fsep{position:absolute;top:18px;width:1px;height:110px;background:rgba(255,255,255,.2)}
.newsletter{position:absolute;left:540px;top:6px;width:220px;height:122px;background:var(--red-box);padding:6px 9px}
.newsletter h4{font-family:"Questrial",sans-serif;font-weight:400;font-size:14px}
.field{display:flex;align-items:center;margin-top:6px;font-size:10.5px}
.field label{width:61px}
.field span{width:144px;height:20px;background:#fff;display:block}
.signup{position:absolute;right:6px;bottom:8px;width:64px;height:24px;border-radius:4px;background:linear-gradient(#2a8be0,#0d4f9c);font-size:11px;font-weight:700;display:flex;align-items:center;justify-content:center}
.copyright{position:absolute;left:57px;top:1176px;font-size:9.5px;color:#8fa3bd}
.copyright b{color:#fff;font-weight:400}
</style>
</head>
<body>
<div class="page">
  <header class="header">
    <div class="logo"><span class="logo-dot"></span><span class="logo-name">Bright Orchid</span></div>
    <div class="banner">
      <h3>The Corvane News Network</h3>
      <ul>
        <li>• 750,000 visitors access network content per month</li>
        <li>• 89,660 subscribers receive email updates</li>
        <li>• 10,000+ domains access network content</li>
        <li>• Advertising Opportunities</li>
        <li>• Content Management &amp; Delivery</li>
        <li>• Press Release Distribution</li>
      </ul>
      <svg class="banner-bars" width="78" height="40" viewBox="0 0 78 40"><rect x="6" y="28" width="10" height="12" fill="#1c6fb5"/><rect x="20" y="20" width="10" height="20" fill="#2284d0"/><rect x="34" y="14" width="10" height="26" fill="#2a95e3"/><rect x="48" y="6" width="10" height="34" fill="#33a4f0"/><rect x="62" y="0" width="10" height="40" fill="#3fb2fa"/></svg>
    </div>
  </header>
  <nav class="nav">
    <a class="home" href="#">HOME</a>
    <a class="item" href="#">ABOUT US</a>
    <a class="item" href="#">TECH RESOURCES</a>
    <a class="item" href="#" style="margin-left:50px">CONTACT US</a>
    <div class="search"><svg width="13" height="13" viewBox="0 0 13 13"><circle cx="5.5" cy="5.5" r="4" fill="none" stroke="#1a7fd4" stroke-width="2"/><line x1="8.5" y1="8.5" x2="12" y2="12" stroke="#1a7fd4" stroke-width="2.2"/></svg></div>
  </nav>

  <main class="main">
    <article class="post"><h2>The world of opportunities</h2><div class="thumb" role="img" aria-label="Post thumbnail: scattered metallic digits on teal"></div><div class="excerpt"><p>Lorem ipsum dolor sit amet conse ctetuer adipiscing elit. Praeslum molestie lacu-sean nonummyendrerit mauselius porta. Fusce suscipit varius mium sociis natus.</p><p>Fuscefeu giat malesuada odiorbi nunc odio gravitcursus necuctus a loremecenas tristique orci ac sem. Duis ultricies pharetra magn accumsan malesuada orci.</p></div><div class="more">Read More</div><div class="share"><i style="background:#e33"></i>SHARE&nbsp;&nbsp;&nbsp;&nbsp;&nbsp;<i style="background:#39f"></i><i style="background:#36c"></i><i style="background:#b3c"></i></div></article>
    <article class="post"><h2>The world of opportunities</h2><div class="thumb" role="img" aria-label="Post thumbnail: scattered metallic digits on teal"></div><div class="excerpt"><p>Lorem ipsum dolor sit amet conse ctetuer adipiscing elit. Praeslum molestie lacu-sean nonummyendrerit mauselius porta. Fusce suscipit varius mium sociis natus.</p><p>Fuscefeu giat malesuada odiorbi nunc odio gravitcursus necuctus a loremecenas tristique orci ac sem. Duis ultricies pharetra magn accumsan malesuada orci.</p></div><div class="more">Read More</div><div class="share"><i style="background:#e33"></i>SHARE&nbsp;&nbsp;&nbsp;&nbsp;&nbsp;<i style="background:#39f"></i><i style="background:#36c"></i><i style="background:#b3c"></i></div></article>
    <article class="post"><h2>The world of opportunities</h2><div class="thumb" role="img" aria-label="Post thumbnail: scattered metallic digits on teal"></div><div class="excerpt"><p>Lorem ipsum dolor sit amet conse ctetuer adipiscing elit. Praeslum molestie lacu-sean nonummyendrerit mauselius porta. Fusce suscipit varius mium sociis natus.</p><p>Fuscefeu giat malesuada odiorbi nunc odio gravitcursus necuctus a loremecenas tristique orci ac sem. Duis ultricies pharetra magn accumsan malesuada orci.</p></div><div class="more">Read More</div><div class="share"><i style="background:#e33"></i>SHARE&nbsp;&nbsp;&nbsp;&nbsp;&nbsp;<i style="background:#39f"></i><i style="background:#36c"></i><i style="background:#b3c"></i></div></article>
    <article class="post"><h2>The world of opportunities</h2><div class="thumb" role="img" aria-label="Post thumbnail: scattered metallic digits on teal"></div><div class="excerpt"><p>Lorem ipsum dolor sit amet conse ctetuer adipiscing elit. Praeslum molestie lacu-sean nonummyendrerit mauselius porta. Fusce suscipit varius mium sociis natus.</p><p>Fuscefeu giat malesuada odiorbi nunc odio gravitcursus necuctus a loremecenas tristique orci ac sem. Duis ultricies pharetra magn accumsan malesuada orci.</p></div><div class="more">Read More</div><div class="share"><i style="background:#e33"></i>SHARE&nbsp;&nbsp;&nbsp;&nbsp;&nbsp;<i style="background:#39f"></i><i style="background:#36c"></i><i style="background:#b3c"></i></div></article>
    <article class="post"><h2>The world of opportunities</h2><div class="thumb" role="img" aria-label="Post thumbnail: scattered metallic digits on teal"></div><div class="excerpt"><p>Lorem ipsum dolor sit amet conse ctetuer adipiscing elit. Praeslum molestie lacu-sean nonummyendrerit mauselius porta. Fusce suscipit varius mium sociis natus.</p><p>Fuscefeu giat malesuada odiorbi nunc odio gravitcursus necuctus a loremecenas tristique orci ac sem. Duis ultricies pharetra magn accumsan malesuada orci.</p></div><div class="more">Read More</div><div class="share"><i style="background:#e33"></i>SHARE&nbsp;&nbsp;&nbsp;&nbsp;&nbsp;<i style="background:#39f"></i><i style="background:#36c"></i><i style="background:#b3c"></i></div></article>
    <article class="post"><h2>The world of opportunities</h2><div class="thumb" role="img" aria-label="Post thumbnail: scattered metallic digits on teal"></div><div class="excerpt"><p>Lorem ipsum dolor sit amet conse ctetuer adipiscing elit. Praeslum molestie lacu-sean nonummyendrerit mauselius porta. Fusce suscipit varius mium sociis natus.</p><p>Fuscefeu giat malesuada odiorbi nunc odio gravitcursus necuctus a loremecenas tristique orci ac sem. Duis ultricies pharetra magn accumsan malesuada orci.</p></div><div class="more">Read More</div><div class="share"><i style="background:#e33"></i>SHARE&nbsp;&nbsp;&nbsp;&nbsp;&nbsp;<i style="background:#39f"></i><i style="background:#36c"></i><i style="background:#b3c"></i></div></article>
  </main>

  <div class="divider"></div>

  <aside class="side">
    <div class="social">
      <span style="background:#4fb3e0"></span><span style="background:#555"></span><span style="background:#3b5b9e"></span><span style="background:#2f6fb0"></span><span style="background:#3aa43a"></span><span style="background:#f3b520"></span><span style="background:#3cb43c"></span>
    </div>
    <div class="callout" style="top:182px"><i style="background:#f08a1c"></i>SUBSCRIBE TO OUR RSS FEED!</div>
    <div class="callout" style="top:229px"><i style="background:#36a3e6"></i>FOLLOW US ON CHIRPLINE!</div>

    <div class="tabs">
      <div class="tab-row"><span class="on">Category</span><span class="gap">Archives</span><span class="gap">Comments</span></div>
      <div class="tab-body">
        <ul class="arrow-list">
          <li>Browsers</li><li>Computers</li><li>Featured</li><li>General</li><li>News</li><li>Parent Categor</li><li>Child Category</li><li>Tech</li><li>Lorem Ipsum is simply</li>
        </ul>
      </div>
    </div>

    <div class="panel-head" style="top:478px">Featured Posts</div>
    <ul class="arrow-list featured">
      <li>Sample post with, links, paragraphs and com-ments..</li>
      <li>This is Just Going To Be Another Test Post..</li>
      <li>Keeping The Title Length Equal For Home..</li>
      <li>Another One to Fill Space..</li>
      <li>This Is Going To Be A Decent Length Title With Little Text..</li>
    </ul>

    <div class="panel-head" style="top:650px">Orchid Circle Friends &amp; Fans</div>
    <div class="photo" role="img" aria-label="Photo of a group of friends in front of a clock tower"></div>
    <div class="badge" style="left:31px;background:linear-gradient(#e9f2fa,#2c7bc4);border:1px solid #9ab"></div>
    <div class="badge" style="left:132px;background:#2b1214;border:1px solid #600"></div>
  </aside>

  <footer class="footer">
    <div class="fcol" style="left:12px"><h4>Reviews</h4><ul><li>Tech</li><li>online marketing</li><li>Affiliation</li><li>Making Money</li></ul></div>
    <div class="fsep" style="left:120px"></div>
    <div class="fcol" style="left:142px"><h4>News</h4><ul><li>Business Tech</li><li>Corrections</li><li>Crave</li><li>Green Tech</li><li>Wireless</li></ul></div>
    <div class="fsep" style="left:238px"></div>
    <div class="fcol" style="left:261px"><h4>Downloads</h4><ul><li>Windows</li><li>Mac</li><li>Webware</li><li>All Downloads</li><li>Add your software</li></ul></div>
    <div class="fsep" style="left:374px"></div>
    <div class="fcol" style="left:398px;width:130px"><h4>More</h4><ul><li>About Techvane</li><li>Techvane Forums</li><li>About Halverd Interactive</li><li>Center</li><li>Customer Help</li></ul></div>
    <div class="newsletter">
      <h4>Newsletter</h4>
      <div class="field"><label>Emial id</label><span></span></div>
      <div class="field"><label>Password</label><span></span></div>
      <div class="signup">Sign Up ▸</div>
    </div>
  </footer>
</div>
<div class="copyright">Copyright © <b>Bright Orchid</b></div>
</body>
</html>
```